Consulting company with focus on aviation needs

We need a new business card design for our company. The company consults with multiple players in the industry like manufacturers and airlines. It is also a supplier and an inter-company level. Given the targeted industry (aviation) it should be both kind of serious, sound, secure, classy, ​​but also a bit technical, innovative. Should not be too playful, however, "fresh", "airy", "ligth" and "suprising" are suitabe attributes. The existing logo shall be used.

Airlines

```html
<!DOCTYPE html>
<html lang="en">
<head>
<meta charset="utf-8">
<title>Velora – Business Card</title>
<link rel="stylesheet" href="https://fonts.googleapis.com/css2?family=Open+Sans:wght@400;600&family=Questrial&display=swap">
<style>
  :root {
    --teal: #1b9e83;
    --green: #98bd5b;
    --orange: #f39b2c;
    --slate: #6c6f6c;
    --slate-dark: #5f625f;
    --paper: #ffffff;
    --paper-cool: #f2f2f2;
    --stage: #e8e5e2;
    --ink-light: #ffffff;
  }
  * { box-sizing: border-box; margin: 0; padding: 0; }
  html, body { width: 1200px; height: 900px; overflow: hidden; }
  body { background: var(--stage); font-family: "Open Sans", sans-serif; position: relative; }

  .card { position: absolute; overflow: hidden; box-shadow: 0 6px 18px rgba(0,0,0,.18); }

  /* Front */
  .card-front { left: 78px; top: 33px; width: 588px; height: 365px; background: var(--paper); }
  .brand { position: absolute; display: flex; align-items: center; gap: 18px; }
  .card-front .brand { left: 80px; top: 52px; }
  .brand-dot { width: 96px; height: 96px; border-radius: 50%; background: var(--teal); flex: none; }
  .brand-name { font-family: "Open Sans", sans-serif; font-weight: 600; color: var(--slate); font-size: 46px; letter-spacing: 6px; line-height: 1; }
  .tagline { font-family: "Open Sans", sans-serif; font-weight: 600; color: var(--orange); font-size: 17px; margin-top: 8px; letter-spacing: .2px; white-space: nowrap; }

  .band { position: absolute; left: 0; top: 180px; width: 588px; height: 185px; }

  .contacts { position: absolute; left: 30px; top: 256px; list-style: none; color: var(--ink-light); font-size: 15px; line-height: 21.3px; }
  .contacts li { display: flex; align-items: center; gap: 8px; }
  .contacts svg { width: 12px; height: 12px; flex: none; fill: var(--ink-light); }

  .person { position: absolute; right: 36px; top: 236px; text-align: right; color: var(--ink-light); }
  .person-name { font-family: "Questrial", sans-serif; font-size: 23px; line-height: 28px; }
  .person-role { font-size: 15px; line-height: 20px; }
  .person-address { font-size: 15px; line-height: 21px; margin-top: 9px; }

  /* Back */
  .card-back { left: 388px; top: 505px; width: 568px; height: 352px; background: var(--paper-cool); }
  .back-texture { position: absolute; inset: 0; background: linear-gradient(160deg, #f7f7f7 0%, #e6e6e6 55%, #f3f3f3 100%); }
  .back-brand { position: absolute; left: 0; right: 0; top: 80px; display: flex; flex-direction: column; align-items: center; }
  .back-brand .brand-dot { width: 100px; height: 100px; }
  .back-brand .brand-name { font-size: 44px; margin-top: 22px; }
  .back-brand .tagline { font-size: 16px; margin-top: 4px; }
</style>
</head>
<body>

<section class="card card-front" aria-label="Business card front">
  <div class="brand">
    <span class="brand-dot"></span>
    <div>
      <div class="brand-name">VELORA</div>
      <div class="tagline">Trusted Partners - Smarter Aviation</div>
    </div>
  </div>

  <svg class="band" viewBox="0 0 588 185" aria-hidden="true">
    <polygon points="0,9 147,9 127,35 0,35" fill="var(--teal)"/>
    <polygon points="152,9 272,9 252,35 132,35" fill="var(--green)"/>
    <polygon points="277,9 397,9 377,35 257,35" fill="var(--orange)"/>
    <polygon points="417,0 588,0 588,185 0,185 0,35 392,35" fill="var(--slate)"/>
    <line x1="0" y1="35" x2="392" y2="35" stroke="var(--slate-dark)" stroke-width="1"/>
  </svg>

  <ul class="contacts">
    <li><svg viewBox="0 0 12 12"><rect x="3" y="0" width="6" height="12" rx="1"/><rect x="4" y="1.5" width="4" height="7.5" fill="var(--slate)"/></svg>041-555 207 318</li>
    <li><svg viewBox="0 0 12 12"><path d="M1 4c0-2 3-3 5-3s5 1 5 3v1H8V3.5H4V5H1z"/><rect x="2" y="6" width="8" height="5" rx="1"/></svg>041-555 207 318</li>
    <li><svg viewBox="0 0 12 12"><rect x="0.5" y="2" width="11" height="8"/><path d="M0.5 2l5.5 4.5L11.5 2" fill="none" stroke="var(--slate)" stroke-width="1"/></svg>info@veloraconsult.com</li>
    <li><svg viewBox="0 0 12 12"><circle cx="6" cy="6" r="5.5"/><path d="M3 4l3 1 1 3-2 2M7 2l2 2" fill="none" stroke="var(--slate)" stroke-width="1"/></svg>www.veloraconsult.com</li>
  </ul>

  <div class="person">
    <div class="person-name">Daniel Harper</div>
    <div class="person-role">Managing Director</div>
    <div class="person-address">12345, Address Goes Here<br>Country Name, 123456.</div>
  </div>
</section>

<section class="card card-back" aria-label="Business card back">
  <div class="back-texture" role="img" aria-label="Faint repeating pattern of the company emblem across the card"></div>
  <div class="back-brand">
    <span class="brand-dot"></span>
    <div class="brand-name">VELORA</div>
    <div class="tagline">Trusted Partners - Smarter Aviation</div>
  </div>
</section>

</body>
</html>
```